FLX & Harwick Solutions Business Card Design

a specialised consulting company, aviation specialist, like to have use blue colour on white background.
back of card to have printed-
NDT Expertise:
INSPECTION & TESTING CONSULTING
TRAINING & EDUCATION
CERTIFICATION SERVICES
LEVEL 3 SERVICES
VORTEM / AUDITING
INSPECTION SYSTEMS

Target Market(s)

Mainly the aerospace industry, manufacturers and airframe/engine overhaul companies.

Industry/Entity Type

Business

Contact Information for Business Card

FLX & Harwick Solutions

Derek Lomaxe JP

+61 (0)491570147
flxharwicksolutions@mailbox-demo.net

Font styles to use
Serif

Colors
3276b4
32a5d5

Requirements
Must have
• aviation style logo with letters FHS part of or adjacent to.

then company name: FLX & Harwick Solutions

then name in slightly smaller font : Derek Lomaxe JP

then phone and email details

Back of card, as per brief, but all text to be centred

```html
<!DOCTYPE html>
<html lang="en">
<head>
<meta charset="utf-8">
<title>FLX &amp; Harwick Solutions – Business Card</title>
<link rel="stylesheet" href="https://fonts.googleapis.com/css2?family=Questrial&display=swap">
<style>
  :root {
    --brand-blue: #1e4582;
    --paper: #ffffff;
    --backdrop: #e6e7ea;
    --card-shadow: rgba(20, 30, 50, 0.22);
  }
  * { margin: 0; padding: 0; box-sizing: border-box; }
  html, body {
    width: 1200px;
    height: 900px;
    overflow: hidden;
    background: var(--backdrop);
    font-family: "Questrial", "Century Gothic", sans-serif;
  }
  .canvas {
    position: relative;
    width: 1200px;
    height: 900px;
  }
  .card {
    position: absolute;
    width: 580px;
    height: 330px;
    box-shadow: 0 10px 28px var(--card-shadow);
    overflow: hidden;
  }

  /* Back of card */
  .card--back {
    left: 70px;
    top: 100px;
    background: var(--brand-blue);
    color: var(--paper);
    text-align: center;
  }
  .card--back .brand { margin-top: 58px; }
  .services {
    margin: 34px auto 0;
    width: 440px;
    font-size: 17px;
    line-height: 1.45;
    letter-spacing: 0.2px;
  }

  /* Brand lockup (text only) */
  .brand {
    display: inline-block;
    text-align: left;
    line-height: 1;
  }
  .brand__main {
    display: block;
    font-size: 84px;
    letter-spacing: -2px;
  }
  .brand__sub {
    display: block;
    margin-top: 4px;
    padding-left: 40px;
    font-size: 19px;
    letter-spacing: 0.6px;
    text-transform: uppercase;
  }

  /* Front of card */
  .card--front {
    left: 550px;
    top: 470px;
    background: var(--paper);
    color: var(--brand-blue);
  }
  .card--front .brand {
    position: absolute;
    left: 150px;
    top: 50px;
  }
  .holder {
    position: absolute;
    left: 52px;
    top: 218px;
    font-size: 22px;
  }
  .holder__title {
    display: block;
    text-align: right;
    font-size: 12px;
    margin-top: 2px;
  }
  .contact {
    position: absolute;
    left: 250px;
    top: 190px;
    font-size: 13px;
    line-height: 1.7;
    list-style: none;
  }
  .band {
    position: absolute;
    left: 0;
    bottom: 0;
    width: 100%;
    height: 22px;
    background: var(--brand-blue);
  }
</style>
</head>
<body>
<main class="canvas">

  <section class="card card--back" aria-label="Back of business card">
    <div class="brand">
      <span class="brand__main">FLX</span>
      <span class="brand__sub">&amp; Harwick Solutions</span>
    </div>
    <p class="services">
      Inspection &amp; Testing Consulting | Training &amp; Education
      Certification Services | Level 3 Services | VORTEM/Auditing
      Inspection Systems
    </p>
  </section>

  <section class="card card--front" aria-label="Front of business card">
    <div class="brand">
      <span class="brand__main">FLX</span>
      <span class="brand__sub">&amp; Harwick Solutions</span>
    </div>
    <p class="holder">Derek Lomaxe<span class="holder__title">JP</span></p>
    <ul class="contact">
      <li>P: +61 (0)491570147</li>
      <li>E: flxharwicksolutions@mailbox-demo.net</li>
    </ul>
    <div class="band"></div>
  </section>

</main>
</body>
</html>
```